Stonvale Depot needs a Self-Mailer Brochure Design

NOTE: DO NOT COPY OUR CURRENT BROCHURE DESIGN, WE DON'T LIKE IT AND LOOKING FOR SOMETHING NEW.

I am in charge of marketing at Stonvale Depot. I need create a new self-mailer brochure with our products.

Brief introduction:
• We are wholesaler specializing in home hardware and building supplies. We sell high-end products at better prices.
• Here's some of the items we sell: Bathtub Sales, Faucet Sales, Range Hood
Sales, Shower Sales, Sink Sales, Toilet Sales, Tile Sales, Kitchen supply
sales, Bathroom Supply Sales, Vanities, Lighting, Door Hardware, Mouldings etc.
• Areas Served: Greater Phoenix Area. We are trying to target local businesses in the Phoenix area. Our zip code is 85040.

We would like to create a new self-mailer brochure, that is going to
list our products. The current self-mailer brochure we have is not as organized as we need it to be. We need to make it well-organized and more efficient for our potential customers. I'm attaching our current self-mailer brochure as a reference, Please see the current self-mailer brochure to get an idea of what we need exactly, it will help you to come up with a better concept of putting it all together.

• On the first page, we'd like to include all the essential information about us, and our products- our logo and address, the discounts we provide, and the variety of products that we offer.
• On the other pages, we'd like to list our products with images and descriptions, just like in the current brochure.
• Please make it look appealing to the customer, start the listing with vanities/faucets/surfaces etc.
• You could include the "compare prices" section, just like in current brochure, but only on the first page, instead of every item (Our competitor is Drent, you can find it in the current brochure)
• We're open to suggestions, so please advise on the design (Simple clean lines, high-end, luxury theme would work best)
• Also, it is important to include all the necessary requirements for a self-mailer so we meet the required specification (you can find the requirements online)

Please find all the imagery and descriptions on our website- https://www.stonvaledepot-example.com/ - all the images in high res.
The format is 8/5X11", 2 pages, on both sides.

Please email me at quietlark.mira@mailtrove-example.com, or text me through the platform if you have any questions!
Current brochure and logo are attached,

Looking forward to hear back from you!

Mira

Target Market(s)

Local Businesses in Phoenix

Industry/Entity Type

Building Product

Font styles to use
Serif

Colors
abd036
000000
5c5c5c
ffffff

Requirements
Must have
• We would like to create a new self-mailer brochure, that is going to
• list our products. The current self-mailer brochure we have is not as organized as we need it to be. We need to make it well-organized and more efficient for our potential customers. I'm attaching our current self-mailer brochure as a reference, Please see the current self-mailer brochure to get an idea of what we need exactly, it will help you to come up with a better concept of putting it all together.
• • On the first page, we'd like to include all the essential information about us, and our products- our logo and address, the discounts we provide, and the variety of products that we offer.
• • On the other pages, we'd like to list our products with images and descriptions, just like in the current brochure.
• • Please make it look appealing to the customer, start the listing with vanities/faucets/surfaces etc. by category (check our website to get familiar with categories)
• • You could include the "compare prices" section, just like in current brochure, but only on the first page, instead of every item (Our competitor is Drent, you can find it in the current brochure)
• • We're open to suggestions, so please advise on the design (Simple clean lines, high-end, luxury theme would work best)
• • Also, it is important to include all the necessary requirements for a self-mailer so we meet the required specification (you can find the requirements online)

```html
<!DOCTYPE html>
<html lang="en">
<head>
<meta charset="utf-8">
<title>Stonvale Depot – Self-Mailer Brochure</title>
<link href="https://fonts.googleapis.com/css2?family=Lora:wght@400;600;700&family=Playfair+Display:wght@600;700&display=swap" rel="stylesheet">
<style>
  :root {
    --lime: #abd036;
    --ink: #000000;
    --grey: #5c5c5c;
    --paper: #ffffff;
    --backdrop: #e4e3e6;
    --rule: #d6d6d6;
    --soft: #f4f6ee;
  }
  * { box-sizing: border-box; margin: 0; padding: 0; }
  html, body { width: 1200px; height: 1200px; overflow: hidden; }
  body {
    background: var(--backdrop);
    font-family: "Lora", serif;
    color: var(--ink);
    display: flex;
    align-items: center;
    justify-content: center;
  }
  .spread { display: flex; box-shadow: 0 10px 30px rgba(0,0,0,.12); }
  .page {
    width: 560px;
    height: 790px;
    background: var(--paper);
    padding: 26px;
    display: flex;
    flex-direction: column;
  }
  .page + .page { border-left: 1px solid #e6e6e6; }
  .display { font-family: "Playfair Display", serif; }

  /* ---------- Front / mailer page ---------- */
  .brand-bar {
    display: flex;
    align-items: center;
    justify-content: space-between;
    border-bottom: 2px solid var(--lime);
    padding-bottom: 12px;
  }
  .brand { display: flex; align-items: center; gap: 10px; }
  .brand-mark { width: 22px; height: 22px; background: var(--lime); }
  .brand-name { font-family: "Playfair Display", serif; font-weight: 700; font-size: 26px; letter-spacing: .5px; }
  .brand-contact { text-align: right; font-size: 9.5px; line-height: 1.5; color: var(--grey); }
  .tagline { font-size: 10px; letter-spacing: 2px; text-transform: uppercase; color: var(--grey); margin-top: 8px; }

  .offer {
    margin-top: 14px;
    background: var(--ink);
    color: var(--paper);
    padding: 14px 18px;
    display: flex;
    align-items: center;
    justify-content: space-between;
  }
  .offer-title { font-family: "Playfair Display", serif; font-size: 24px; font-weight: 700; line-height: 1.1; }
  .offer-title span { color: var(--lime); }
  .offer-note { font-size: 9.5px; line-height: 1.5; max-width: 190px; text-align: right; }

  .section-label {
    font-family: "Playfair Display", serif;
    font-size: 14px;
    font-weight: 700;
    text-transform: uppercase;
    letter-spacing: 1.5px;
    margin: 14px 0 7px;
    display: flex;
    align-items: center;
    gap: 8px;
  }
  .section-label::after { content: ""; flex: 1; height: 1px; background: var(--rule); }

  .range-list {
    display: grid;
    grid-template-columns: repeat(4, 1fr);
    gap: 5px 10px;
    font-size: 10px;
    list-style: none;
  }
  .range-list li { display: flex; align-items: center; gap: 6px; }
  .range-list li::before { content: ""; width: 6px; height: 6px; background: var(--lime); flex: none; }

  .compare { width: 100%; border-collapse: collapse; font-size: 10px; }
  .compare th {
    background: var(--lime);
    color: var(--ink);
    font-weight: 700;
    text-align: left;
    padding: 5px 8px;
  }
  .compare td { padding: 4px 8px; border-bottom: 1px solid var(--rule); }
  .compare .num { text-align: right; white-space: nowrap; }
  .compare .theirs { color: var(--grey); text-decoration: line-through; }
  .compare .ours { font-weight: 700; }

  .mailer {
    margin-top: auto;
    border: 1px dashed var(--grey);
    height: 200px;
    padding: 12px 14px;
    position: relative;
    font-size: 9.5px;
    line-height: 1.45;
  }
  .return-address { color: var(--grey); }
  .return-address strong { color: var(--ink); font-family: "Playfair Display", serif; font-size: 12px; }
  .indicia {
    position: absolute;
    top: 12px;
    right: 14px;
    width: 108px;
    border: 1px solid var(--ink);
    text-align: center;
    font-size: 8.5px;
    line-height: 1.35;
    padding: 6px 4px;
    text-transform: uppercase;
  }
  .recipient {
    position: absolute;
    left: 200px;
    top: 100px;
    font-size: 10.5px;
    line-height: 1.55;
  }
  .recipient .route { font-size: 8.5px; color: var(--grey); letter-spacing: 1px; }
  .mailer-rule {
    position: absolute;
    left: 14px;
    right: 14px;
    top: 86px;
    border-top: 1px solid var(--rule);
  }

  /* ---------- Product page ---------- */
  .category + .category { margin-top: 16px; }
  .category-band {
    background: var(--lime);
    height: 30px;
    display: flex;
    align-items: center;
    justify-content: space-between;
    padding: 0 12px;
    color: var(--ink);
  }
  .category-band h2 { font-family: "Playfair Display", serif; font-size: 17px; font-weight: 700; letter-spacing: 2px; text-transform: uppercase; }
  .category-band a { font-size: 9px; color: var(--ink); text-decoration: none; }
  .products { display: grid; grid-template-columns: repeat(3, 1fr); margin-top: 10px; }
  .product { padding: 0 9px; display: flex; flex-direction: column; }
  .product:first-child { padding-left: 0; }
  .product:last-child { padding-right: 0; }
  .product + .product { border-left: 1px solid var(--rule); }
  .product-image { width: 100%; height: 112px; margin-bottom: 7px; }
  .tone-steel { background: linear-gradient(135deg, #f2f2f2, #b9bcc0 60%, #8d9196); }
  .tone-room { background: linear-gradient(135deg, #8a7d6d, #d8d2c9 55%, #f3f1ee); }
  .tone-dark { background: linear-gradient(135deg, #2a2a2c, #8b8d90 55%, #eeeeee); }
  .tone-navy { background: linear-gradient(160deg, #1f2a4a, #3a4466 50%, #f1f1f1); }
  .tone-white { background: linear-gradient(135deg, #ffffff, #e2e2e2 60%, #c7c7c7); }
  .tone-wood { background: linear-gradient(90deg, #9c968d, #c9c3b9 40%, #7f7a73 70%, #b3ada4); }
  .tone-tile { background: linear-gradient(135deg, #9a9a9a, #d6d6d6 50%, #a8a8a8); }
  .product-name { font-size: 9.5px; font-weight: 600; line-height: 1.35; min-height: 39px; }
  .product-price {
    display: flex;
    justify-content: space-between;
    align-items: baseline;
    border-top: 1px solid var(--rule);
    padding-top: 4px;
    margin-top: 3px;
  }
  .price-now { font-family: "Playfair Display", serif; font-size: 15px; font-weight: 700; }
  .save-pct { font-size: 9.5px; font-weight: 700; color: var(--ink); background: var(--lime); padding: 1px 5px; }
  .page-foot {
    margin-top: auto;
    display: flex;
    justify-content: space-between;
    font-size: 9px;
    color: var(--grey);
    border-top: 1px solid var(--rule);
    padding-top: 7px;
  }
</style>
</head>
<body>
<div class="spread">

  <section class="page page-front">
    <header class="brand-bar">
      <div class="brand">
        <span class="brand-mark"></span>
        <span class="brand-name">Stonvale Depot</span>
      </div>
      <address class="brand-contact">
        4120 E Broadway Rd, Phoenix, AZ 85040<br>
        (602) 555-0148 · www.stonvaledepot-example.com
      </address>
    </header>
    <p class="tagline">Wholesale home hardware &amp; building supplies · Greater Phoenix</p>

    <div class="offer">
      <p class="offer-title">High-end products.<br><span>Up to 70% off</span> retail.</p>
      <p class="offer-note">Contractor and business pricing on every order. Volume discounts for local Phoenix businesses.</p>
    </div>

    <h3 class="section-label">Our Range</h3>
    <ul class="range-list">
      <li>Vanities</li><li>Faucets</li><li>Tile &amp; Surfaces</li><li>Sinks</li>
      <li>Showers</li><li>Bathtubs</li><li>Toilets</li><li>Range Hoods</li>
      <li>Kitchen Supply</li><li>Lighting</li><li>Door Hardware</li><li>Mouldings</li>
    </ul>

    <h3 class="section-label">Compare Prices</h3>
    <table class="compare">
      <thead>
        <tr><th>Product</th><th class="num">Drent</th><th class="num">Stonvale</th><th class="num">You Save</th></tr>
      </thead>
      <tbody>
        <tr><td>Arlo 60" Double Sink Vanity Set</td><td class="num theirs">$1,974</td><td class="num ours">$875.00</td><td class="num">56%</td></tr>
        <tr><td>Pull-Down Kitchen Faucet</td><td class="num theirs">$119.00</td><td class="num ours">$54.95</td><td class="num">54%</td></tr>
        <tr><td>Farmhouse Double Bowl Sink</td><td class="num theirs">$119.00</td><td class="num ours">$57.95</td><td class="num">51%</td></tr>
        <tr><td>Hexagonal Marble Mosaic Tile</td><td class="num theirs">$17.99</td><td class="num ours">$7.95</td><td class="num">56%</td></tr>
        <tr><td>Meridian Hall &amp; Closet Lever</td><td class="num theirs">$36.97</td><td class="num ours">$15.95</td><td class="num">59%</td></tr>
      </tbody>
    </table>

    <div class="mailer">
      <p class="return-address">
        <strong>Stonvale Depot</strong><br>
        4120 E Broadway Rd<br>
        Phoenix, AZ 85040
      </p>
      <div class="indicia">Presorted Standard<br>US Postage Paid<br>Phoenix, AZ<br>Permit No. 000</div>
      <div class="mailer-rule"></div>
      <p class="recipient">
        <span class="route">ECRWSS · LOCAL BUSINESS CUSTOMER</span><br>
        Business Name<br>
        Street Address<br>
        Phoenix, AZ 85000
      </p>
    </div>
  </section>

  <section class="page page-products">
    <article class="category">
      <div class="category-band"><h2>Vanities</h2><a>www.stonvaledepot-example.com</a></div>
      <div class="products">
        <div class="product">
          <div class="product-image tone-dark" role="img" aria-label="Photo of a dark double sink vanity with mirror"></div>
          <p class="product-name">Arlo 60" Double Sink Vanity Set (includes mirror)</p>
          <p class="product-price"><span class="price-now">$875.00</span><span class="save-pct">56% off</span></p>
        </div>
        <div class="product">
          <div class="product-image tone-dark" role="img" aria-label="Photo of an espresso single sink vanity with mirror"></div>
          <p class="product-name">Arlo 36" Single Sink Vanity Set – Espresso</p>
          <p class="product-price"><span class="price-now">$560.00</span><span class="save-pct">64% off</span></p>
        </div>
        <div class="product">
          <div class="product-image tone-navy" role="img" aria-label="Photo of a white double sink vanity with two mirrors"></div>
          <p class="product-name">Castel 72" Double Sink Vanity with Bottom Rack</p>
          <p class="product-price"><span class="price-now">$1,089.00</span><span class="save-pct">41% off</span></p>
        </div>
      </div>
    </article>

    <article class="category">
      <div class="category-band"><h2>Faucets</h2><a>www.stonvaledepot-example.com</a></div>
      <div class="products">
        <div class="product">
          <div class="product-image tone-steel" role="img" aria-label="Photo of a brushed nickel shower faucet trim kit"></div>
          <p class="product-name">Single-Lever Concealed Shower Trim Kit (Brushed Nickel)</p>
          <p class="product-price"><span class="price-now">$57.95</span><span class="save-pct">51% off</span></p>
        </div>
        <div class="product">
          <div class="product-image tone-room" role="img" aria-label="Photo of a pull-down brushed nickel kitchen faucet"></div>
          <p class="product-name">Pull-Down Single Handle Kitchen Faucet (Brushed Nickel)</p>
          <p class="product-price"><span class="price-now">$54.95</span><span class="save-pct">54% off</span></p>
        </div>
        <div class="product">
          <div class="product-image tone-white" role="img" aria-label="Photo of a body shower tower panel with spray wand"></div>
          <p class="product-name">59 in. 110-Jet Body Shower Tower with Rain Head</p>
          <p class="product-price"><span class="price-now">$169.00</span><span class="save-pct">45% off</span></p>
        </div>
      </div>
    </article>

    <article class="category">
      <div class="category-band"><h2>Surfaces</h2><a>www.stonvaledepot-example.com</a></div>
      <div class="products">
        <div class="product">
          <div class="product-image tone-wood" role="img" aria-label="Photo of weathered wood-look ceramic plank tile"></div>
          <p class="product-name">Weathered Ceramic Hardwood Plank Look 18 x 36 in. Tile</p>
          <p class="product-price"><span class="price-now">$1.99/sqft</span><span class="save-pct">49% off</span></p>
        </div>
        <div class="product">
          <div class="product-image tone-tile" role="img" aria-label="Photo of white marble hexagonal mosaic tile sheet"></div>
          <p class="product-name">White Marble Look Hexagonal Mosaic Tile (1 sq ft sheet)</p>
          <p class="product-price"><span class="price-now">$7.95/sqft</span><span class="save-pct">56% off</span></p>
        </div>
        <div class="product">
          <div class="product-image tone-tile" role="img" aria-label="Photo of a glossy white beveled subway tile"></div>
          <p class="product-name">Glossy White Beveled Subway Tile 3" x 6"</p>
          <p class="product-price"><span class="price-now">$0.19/ea</span><span class="save-pct">34% off</span></p>
        </div>
      </div>
    </article>

    <footer class="page-foot">
      <span>Stonvale Depot · Phoenix, AZ 85040</span>
      <span>More categories at www.stonvaledepot-example.com</span>
    </footer>
  </section>

</div>
</body>
</html>
```